Velvet Crest Car Detailing Brochure

I would like a trifold brochure designed for my car detailing business. The background has to be full black or mostly black with some designing using only colors present in our logo.

Front page must have our logo and name, list of services, a photo and mybe our phone number but no long text.

Inside I want to present each service one by one with its description and a photo representing/showing each service. (I will provide the text below). For photos, use stock photos and I will add come of mines already too.

On the back of the brochure I want to have contact & info: phone number, opening hours, address, website, Instagram.

Outside left I want the text About us and photo/design.

I want the brochure to be neat, professional, easy to read, but at the same time not too boring.

Text:
1. About us
a. the ultimate destination for car care in Geneva. We provide personalized, detail-oriented services that bring out the best in your car. With our expert techniques and dedicated approach, we ensure that your car receives the utmost care and attention. Experience a place where passion meets precision and let us create an exceptional car care experience designed just for you.
2. Services:

DETAILING & HAND WASH

• Comprehensive exterior & interior care
• Personalisation and tailored cleaning packages
• Decontamination
• Premium products
• Attention to detail for a perfect finish

POLISHING

• Eliminates scratches, holograms
• Revives and protects paint
• Ensures lasting gloss
• Enhances paint life
• Preserves car’s value and beauty

CERAMIC TREATMENT

• Durable paint protection
• Water-repellent (hydrophobic) effect
• Easier cleaning, enhanced shine
• Long-term surface safeguarding
• Shields against environmental impacts

DRY ICE WASH

• Innovative, waterless method
• Safe for all car parts
• Deep cleans, removes odors
• Allergen-free, antibacterial
• Gentle, effective
• Advanced cleaning technology

COVERING

• Personalized vehicle styling
• More than 150 colours available
• Clean cut without using a cutter
• High-quality, durable materials
• Custom designs available

PROTECTION FILM

• Invisible, durable shield
• Self-healing technology
• 10-year warranty by QR VONT

DETAILING BOUTIQUE

• Premium brands available
• Buy on site during your visit
• Marble Harbour, Zeb Autos, DRUP Polaro
• Essential for at-home car care
• Perfect for quick touch-ups
(for these three brands you can put their logos

Target Market(s)

Our target market includes car owners of all price ranges, with a special focus on those who are passionate about their vehicles. We cater to clients who value excellent service and results, and seek to maintain their cars in pristine condition.

Industry/Entity Type

Automobile / Car detailing

Colors

Designer to choose colors to be used in the design.

Requirements
Must have
• Brand Consistency: The brochure must adhere to our brand colors and style, particularly utilizing the colors present in our logo. Trifold Layout: The design must be specifically tailored for a trifold brochure format. Legibility: Text must be easy to read against the mostly black background, with appropriate font size and style. Professional Look and Feel: The overall design must convey professionalism while being engaging and not overly complex. Photo representation: each service description should have a phot presenting it.
Should not have
• Overcrowded Design: Avoid cluttering with too much text or too many images. The layout should be clean and easy to navigate. Cartoonish Fonts or Graphics: Avoid using unprofessional or casual fonts and graphics that do not align with the upscale and professional image of our business. Distracting Backgrounds: The background should complement and not overpower the content. Stick to the theme of mostly black with design elements from our logo.

```html
<!DOCTYPE html>
<html lang="en">
<head>
<meta charset="utf-8">
<title>Velvet Crest Car Detailing – Trifold Brochure</title>
<link href="https://fonts.googleapis.com/css2?family=Montserrat:ital,wght@0,300;0,400;0,500;0,700;1,400&display=swap" rel="stylesheet">
<style>
  :root{
    --black:#000;
    --ink:#0b0b0d;
    --white:#fff;
    --blue:#3b8fdc;
    --violet:#8a6fc4;
    --pink:#d8409c;
    --magenta:#8a1a6e;
    --stage:#e4e4e6;
    --logo-grad:linear-gradient(90deg,var(--blue),var(--pink));
  }
  *{margin:0;padding:0;box-sizing:border-box}
  html,body{width:922px;height:1200px;overflow:hidden;background:var(--stage)}
  body{font-family:"Montserrat",Arial,sans-serif;color:var(--white);position:relative}
  .sheet{position:absolute;left:79px;width:764px;height:540px;background:var(--black);overflow:hidden}
  .sheet--outside{top:42px}
  .sheet--inside{top:610px}
  .panel{position:absolute;top:0;height:540px}
  .panel--left{left:0;width:255px}
  .panel--mid{left:255px;width:255px}
  .panel--right{left:510px;width:254px}

  /* photo placeholders */
  .photo{position:absolute}
  .photo--cover-wash{inset:0;background:linear-gradient(180deg,var(--magenta) 0%,#6a2c62 22%,#8c8c90 45%,#3a3a3e 75%,#1b1b1e 100%)}
  .photo--garage{inset:0;background:linear-gradient(160deg,#000 40%,#1e1e22 70%,#3a3a3f 100%)}
  .photo--hood-brush{left:0;top:192px;width:255px;height:348px;background:linear-gradient(180deg,#000 0%,#2c2c30 25%,#6a6a70 55%,#38383c 100%)}
  .photo--studio{inset:0;background:linear-gradient(180deg,#141416 0%,#262629 45%,#1a1a1d 100%)}
  .photo--polisher{left:423px;top:258px;width:87px;height:125px;background:linear-gradient(150deg,#2a2a2e,#4a6f8f 55%,#1a1a1c)}

  /* brand name in place of mark */
  .brand{position:absolute;display:flex;flex-direction:column;align-items:center;gap:10px;text-align:center}
  .brand__dot{width:14px;height:14px;border-radius:50%;background:var(--pink)}
  .brand__name{font-weight:400;color:var(--white);letter-spacing:1px;line-height:1.15}
  .brand--mid{left:0;width:255px;top:190px}
  .brand--mid .brand__name{font-size:26px}
  .brand--right{left:0;width:254px;top:90px}
  .brand--right .brand__name{font-size:26px}

  .contact{position:absolute;left:0;width:255px;top:443px;text-align:center;font-size:14px;line-height:18px}
  .cover-services{position:absolute;left:0;width:254px;top:309px;list-style:none;text-align:center;font-style:italic;font-size:14px;line-height:18px;text-transform:uppercase}
  .phone-bar{position:absolute;left:0;width:254px;top:505px;height:21px;background:var(--logo-grad);font-size:13px;line-height:21px;text-align:center}

  /* inside */
  .about__title{position:absolute;left:22px;top:40px;font-size:35px;font-weight:700;background:var(--logo-grad);-webkit-background-clip:text;background-clip:text;color:transparent}
  .about__text{position:absolute;left:22px;top:104px;width:222px;font-size:8.5px;line-height:11px}

  .panel--services{background:linear-gradient(180deg,var(--blue) 0%,var(--violet) 45%,var(--pink) 100%)}
  .services__title{position:absolute;left:16px;top:40px;font-size:34px;font-weight:700}
  .service{position:absolute}
  .service__name{font-size:16px;font-weight:300;letter-spacing:.5px;text-transform:uppercase}
  .service__list{list-style:none;font-size:8.3px;line-height:11px;margin-top:7px}
  .service__list li::before{content:"• "}
  .panel--services .service{left:16px}
  .service--detailing{top:128px}
  .service--polishing{top:271px;left:0 !important}
  .service--polishing .service__name{display:inline-block;background:var(--white);color:var(--black);padding:5px 16px;width:125px;height:28px}
  .service--polishing .service__list{padding-left:16px;margin-top:10px}
  .service--ceramic{top:424px}
  .thumb-frame{position:absolute;left:412px;top:245px;width:88px;height:105px;border:1px solid var(--white);border-right:none}

  .panel--right .service{left:25px}
  .service__name--grad{background:var(--logo-grad);-webkit-background-clip:text;background-clip:text;color:transparent}
  .service--dryice{top:30px}
  .service--film{top:296px}
  .band{position:absolute;left:0;height:31px;background:linear-gradient(90deg,var(--violet),var(--pink));font-size:16px;font-weight:300;line-height:31px;padding-left:25px;text-transform:uppercase;letter-spacing:.5px}
  .band--covering{top:155px;width:158px}
  .band--boutique{top:403px;width:216px}
  .band-list{position:absolute;left:25px}
  .band-list--covering{top:200px}
  .band-list--boutique{top:445px}
</style>
</head>
<body>

<!-- Outside spread -->
<section class="sheet sheet--outside">
  <div class="panel panel--left">
    <div class="photo photo--cover-wash" role="img" aria-label="Photo of a detailer brushing soapy foam over a car badge"></div>
  </div>

  <div class="panel panel--mid">
    <div class="brand brand--mid">
      <span class="brand__dot"></span>
      <span class="brand__name">VELVET<br>CREST</span>
    </div>
    <address class="contact" style="font-style:normal">
      022 555 01 90<br>hello@velvetcrest.ch<br>www.velvetcrest.ch
    </address>
  </div>

  <div class="panel panel--right">
    <div class="photo photo--garage" role="img" aria-label="Dark photo of a car in a detailing studio"></div>
    <div class="brand brand--right">
      <span class="brand__dot"></span>
      <span class="brand__name">VELVET<br>CREST</span>
    </div>
    <ul class="cover-services">
      <li>Detailing &amp; Hand Wash</li>
      <li>Polishing</li>
      <li>Ceramic Treatment</li>
      <li>Dry Ice Wash</li>
      <li>Covering</li>
      <li>Protection Film</li>
      <li>Detailing Boutique</li>
    </ul>
    <div class="phone-bar">022 555 01 91</div>
  </div>
</section>

<!-- Inside spread -->
<section class="sheet sheet--inside">
  <div class="panel panel--left">
    <h2 class="about__title">ABOUT US</h2>
    <p class="about__text">The ultimate destination for car care in Geneva. We provide personalized, detail-oriented services that bring out the best in your car. With our expert techniques and dedicated approach, we ensure that your car receives the utmost care and attention. Experience a place where passion meets precision and let us create an exceptional car care experience designed just for you.</p>
    <div class="photo photo--hood-brush" role="img" aria-label="Photo of a brush cleaning a foamy car bonnet and badge"></div>
  </div>

  <div class="panel panel--mid panel--services">
    <h2 class="services__title">SERVICES:</h2>
    <div class="service service--detailing">
      <h3 class="service__name">Detailing &amp; Hand Wash</h3>
      <ul class="service__list">
        <li>Comprehensive exterior &amp; interior care</li>
        <li>Personalisation and tailored cleaning packages</li>
        <li>Decontamination</li>
        <li>Premium products</li>
        <li>Attention to detail for a perfect finish</li>
      </ul>
    </div>
    <div class="service service--polishing">
      <h3 class="service__name">Polishing</h3>
      <ul class="service__list">
        <li>Eliminates scratches, holograms</li>
        <li>Revives and protects paint</li>
        <li>Ensures lasting gloss</li>
        <li>Enhances paint life</li>
        <li>Preserves car’s value and beauty</li>
      </ul>
    </div>
    <div class="service service--ceramic">
      <h3 class="service__name">Ceramic Treatment</h3>
      <ul class="service__list">
        <li>Durable paint protection</li>
        <li>Water-repellent (hydrophobic) effect</li>
        <li>Easier cleaning, enhanced shine</li>
        <li>Long-term surface safeguarding</li>
        <li>Shields against environmental impacts</li>
      </ul>
    </div>
  </div>

  <div class="thumb-frame"></div>
  <div class="photo photo--polisher" role="img" aria-label="Photo of a rotary polisher working on car paint"></div>

  <div class="panel panel--right">
    <div class="photo photo--studio" role="img" aria-label="Faint photo of a car and detailing products in a studio"></div>
    <div class="service service--dryice">
      <h3 class="service__name service__name--grad">Dry Ice Wash</h3>
      <ul class="service__list">
        <li>Innovative, waterless method</li>
        <li>Safe for all car parts</li>
        <li>Deep cleans, removes odors</li>
        <li>Allergen-free, antibacterial</li>
        <li>Gentle, effective</li>
        <li>Advanced cleaning technology</li>
      </ul>
    </div>
    <h3 class="band band--covering">Covering</h3>
    <ul class="service__list band-list band-list--covering">
      <li>Personalized vehicle styling</li>
      <li>More than 150 colours available</li>
      <li>Clean cut without using a cutter</li>
      <li>High-quality, durable materials</li>
      <li>Custom designs available</li>
    </ul>
    <div class="service service--film">
      <h3 class="service__name service__name--grad">Protection Film</h3>
      <ul class="service__list">
        <li>Invisible, durable shield</li>
        <li>Self-healing technology</li>
        <li>10-year warranty by QR VONT</li>
      </ul>
    </div>
    <h3 class="band band--boutique">Detailing Boutique</h3>
    <ul class="service__list band-list band-list--boutique">
      <li>Premium brands available</li>
      <li>Buy on site during your visit</li>
      <li>Marble Harbour, Zeb Autos, DRUP Polaro</li>
      <li>Essential for at-home car care</li>
      <li>Perfect for quick touch-ups</li>
    </ul>
  </div>
</section>

</body>
</html>
```